Lomi-Seret - Promote and Support a community

Design a website for Ethiopean Community. the design should be friendly, easy to navigate and maintain the look & feel of the Ethiopian culture. a proposed logo is attached but it can be change according to your recommendations. This is a project we are doing at a discount rate as it supports a weak community.
Please visit their current website http://www.lomi-seret.example.il/index.php?lang=en

Target Market(s)

Community members, potential doners

Industry/Entity Type

community

Number of Pages Required

1 page

Font styles to use
Sans Serif

Requirements
Must have
• easy to navigate friendly interface

```html
<!DOCTYPE html>
<html lang="en">
<head>
<meta charset="utf-8">
<title>Lomi Seret – Health for the Ethiopian Israeli Community</title>
<link href="https://fonts.googleapis.com/css2?family=Montserrat:wght@400;500;600;700;800&display=swap" rel="stylesheet">
<style>
:root{
  --green:#1aa31a;
  --green-dark:#128a12;
  --yellow:#f8c41b;
  --red:#d9262b;
  --cream:#fdf3e6;
  --ink:#1d1d1d;
  --text:#4a4a4a;
  --muted:#9a9a9a;
  --footer:#2b2b2b;
  --white:#ffffff;
}
*{box-sizing:border-box;margin:0;padding:0}
html,body{width:1200px;height:4721px;overflow:hidden}
body{position:relative;font-family:'Montserrat',sans-serif;color:var(--text);background:var(--white)}
.abs{position:absolute}
.center{text-align:center}
a{color:inherit;text-decoration:none}

/* top bar */
.topbar{left:0;top:0;width:1200px;height:37px;background:#fff;font-size:10px;color:#333}
.topbar .item{top:0;height:37px;display:flex;align-items:center;gap:8px}
.topbar b{font-size:13px;color:var(--ink)}
.ico{width:22px;height:22px;border-radius:50%;background:var(--yellow);display:flex;align-items:center;justify-content:center}
.lang{left:1050px;top:0;width:122px;height:37px;background:var(--yellow);color:#fff;display:flex;align-items:center;justify-content:center;gap:8px;font-size:17px}

/* hero */
.hero{left:0;top:37px;width:1200px;height:573px;background:radial-gradient(ellipse at 70% 40%,#6b4a3a 0%,#3a2620 45%,#1e1412 100%)}
.nav{left:22px;top:24px;width:1154px;height:99px;background:#fff;box-shadow:0 2px 10px rgba(0,0,0,.15)}
.nav a{position:absolute;top:0;height:99px;display:flex;align-items:center;font-size:10px;font-weight:600;color:var(--ink);text-transform:uppercase}
.nav a.active::after{content:"";position:absolute;left:0;right:0;bottom:8px;height:4px;background:var(--green);border-radius:2px}
.caret{margin-left:6px;font-size:7px}
.btn{display:flex;align-items:center;justify-content:center;border-radius:20px;color:#fff;font-weight:700;font-size:10px;text-transform:uppercase}
.btn-red{background:var(--red)}
.btn-green{background:var(--green)}
.logo-badge{left:514px;top:0;width:172px;height:172px;border-radius:50%;background:#fff;box-shadow:0 2px 8px rgba(0,0,0,.2);display:flex;align-items:center;justify-content:center;font-weight:700;color:var(--red);font-size:22px}
.hero-line{left:150px;top:268px;width:66px;height:3px;background:var(--yellow)}
.hero h1{left:148px;top:290px;font-size:60px;font-weight:700;color:#fff}
.hero .note{left:150px;top:366px;font-size:12px;color:#fff;font-weight:500}
.hero .tag{left:150px;top:390px;width:640px;font-size:29px;font-weight:600;color:#fff;line-height:1.2}
.stripe{left:0;width:1200px;height:7px;display:flex}
.stripe i{flex:1}
.stripe i:nth-child(1){background:var(--green)}
.stripe i:nth-child(2){background:var(--yellow)}
.stripe i:nth-child(3){background:var(--red)}

/* sections */
.sec-cream{background:var(--cream)}
.eyebrow{font-size:12px;color:var(--muted);width:1200px;left:0}
.sec-title{left:0;width:1200px;font-size:55px;font-weight:700;color:var(--ink)}
.underline{left:570px;width:60px;height:2px;background:var(--yellow)}
.para{font-size:10.5px;line-height:1.75;color:var(--text)}
.para strong{color:var(--ink)}
.frame{background:#fff;box-shadow:0 3px 14px rgba(0,0,0,.08)}
.photo{position:absolute}

/* programs */
.card{top:2422px;width:209px;height:341px;background:#fff;border:1px solid #eee}
.card .photo{left:0;top:0;width:209px;height:167px}
.card h4{position:absolute;left:25px;top:194px;font-size:12.5px;color:var(--ink);font-weight:700;line-height:1.3}
.card p{position:absolute;left:25px;top:242px;width:165px;font-size:10px;line-height:1.7}
.card .more{position:absolute;left:25px;top:300px;font-size:10px;font-weight:700;color:var(--red)}

/* contact form */
.field{background:#fff;font-size:9px;color:#666;padding:8px 14px}

/* footer */
.footer{left:0;top:4199px;width:1200px;height:522px;background:var(--footer);color:#fff}
.fcol{position:absolute;top:90px;font-size:10px;font-weight:600;line-height:26.6px}
.fcol h5{font-size:10px;color:var(--yellow);font-weight:700;text-transform:uppercase}
</style>
</head>
<body>

<!-- top bar -->
<div class="abs topbar">
  <div class="abs item" style="left:62px">Call us at:
    <span class="ico"><svg width="11" height="11" viewBox="0 0 24 24"><path fill="#fff" d="M6.6 10.8a15 15 0 006.6 6.6l2.2-2.2c.3-.3.7-.4 1-.2 1.1.4 2.3.6 3.6.6.6 0 1 .4 1 1V20c0 .6-.4 1-1 1A17 17 0 013 4c0-.6.4-1 1-1h3.5c.6 0 1 .4 1 1 0 1.3.2 2.5.6 3.6.1.3 0 .7-.2 1z"/></svg></span>
    <b>04-5550182</b></div>
  <div class="abs item" style="left:248px">
    <span class="ico"><svg width="11" height="11" viewBox="0 0 24 24"><path fill="#fff" d="M2 5h20v14H2zm2 2v.5l8 5 8-5V7z"/></svg></span>
    <span style="font-size:11px;color:#333">lomiseret@example.org</span></div>
  <div class="abs lang"><svg width="14" height="14" viewBox="0 0 24 24"><circle cx="12" cy="12" r="9" fill="none" stroke="#fff" stroke-width="2"/><circle cx="12" cy="12" r="3" fill="#fff"/></svg>עברית</div>
</div>

<!-- hero -->
<div class="abs hero" role="img" aria-label="Photo of Ethiopian Israeli community members gathered together"></div>
<div class="abs nav">
  <a class="active" style="left:38px">Home</a>
  <a style="left:132px">About<span class="caret">▼</span></a>
  <a style="left:226px">The Community</a>
  <a style="left:372px">Programs<span class="caret">▼</span></a>
  <a style="left:715px">News<span class="caret">▼</span></a>
  <a style="left:803px">Advocacy</a>
  <a style="left:923px">Partners</a>
  <span class="abs btn btn-red" style="left:1028px;top:31px;width:104px;height:36px">Support Us</span>
</div>
<div class="abs logo-badge" style="top:0">Lomi Seret</div>
<div class="abs hero-line"></div>
<h1 class="abs hero h1" style="left:148px;top:290px;font-size:60px;font-weight:700;color:#fff">Lomi Seret</h1>
<div class="abs" style="left:150px;top:366px;font-size:12px;color:#fff;font-weight:500">(“health” in both Amharic &amp; Hebrew)</div>
<div class="abs" style="left:150px;top:392px;width:640px;font-size:29px;font-weight:600;color:#fff;line-height:1.2">is dedicated to improving the health of the Ethiopian Israeli community.</div>
<div class="abs stripe" style="top:610px"><i></i><i></i><i></i></div>

<!-- welcome -->
<section class="abs sec-cream" style="left:0;top:617px;width:1200px;height:946px">
  <div class="abs eyebrow center" style="top:64px">Welcome to</div>
  <h2 class="abs sec-title center" style="top:82px">Lomi Seret</h2>
  <div class="abs underline" style="top:157px"></div>
  <p class="abs para center" style="left:316px;top:176px;width:568px"><strong>Aliyah (immigration) from Ethiopia to Israel and the transition to a sedentary lifestyle has resulted in the emergence of chronic diseases, in particular diabetes.</strong> While only 0.4% of the new immigrants were diagnosed with Type 2 diabetes upon arrival, by the time they had lived in Israel for ten years the figure had risen to 18% – three times as many as in the general population. The incidence of hypertension, obesity, asthma and Type 1 diabetes had also increased dramatically.</p>

  <p class="abs para" style="left:150px;top:356px;width:372px"><strong>Lomi Seret was founded in 1999 by Dr. Miriam Adler, Head of the Endocrinology Unit at the Carmel Valley Medical Center.</strong> Her experience with Ethiopian patients made her realize that medical treatment could not succeed without culturally competent communication. Lomi Seret has developed into a small but dedicated NGO, delivering services throughout Israel with the backing and cooperation of a wide range of local and national bodies, including the Ministry of Health, the Ministry of Immigration, the absorption services, municipalities, the HMOs and hospitals.</p>
  <div class="abs frame" style="left:575px;top:310px;width:478px;height:251px">
    <div class="photo" role="img" aria-label="Group photo of the Lomi Seret team standing together in an office" style="left:22px;top:20px;width:438px;height:211px;background:linear-gradient(135deg,#cfd6d8,#8b9aa0 50%,#5c6a70)"></div>
  </div>

  <div class="abs frame" style="left:147px;top:605px;width:476px;height:249px">
    <div class="photo" role="img" aria-label="Group photo of community volunteers holding a certificate in front of flags" style="left:18px;top:20px;width:440px;height:211px;background:linear-gradient(135deg,#d8d2cc,#9a7e70 50%,#5a4a44)"></div>
  </div>
  <p class="abs para" style="left:672px;top:640px;width:360px">Today the Lomi Seret team comprises eight Ethiopian-Israeli healthcare professionals, three Amharic-speaking medical interpreters and four health promotion specialists familiar with the Ethiopian immigrant community. Organizations within Israel and beyond now look to Lomi Seret's programs for inspiration in their efforts to <strong>develop meaningful prevention strategies for improving the health of immigrants and minority communities.</strong></p>
  <span class="abs btn btn-green" style="left:674px;top:784px;width:207px;height:32px;font-size:9.5px">Learn more about Lomi Seret</span>
</section>

<!-- quote -->
<section class="abs" style="left:0;top:1563px;width:1200px;height:161px;background:#fff">
  <p class="abs center" style="left:260px;top:36px;width:680px;font-size:23px;font-weight:600;color:var(--ink);line-height:1.2"><span style="color:var(--red)">Lomi Seret</span> believes that fostering an informed, active health leadership from within the community itself is key to achieving its goals.</p>
</section>

<!-- meaning -->
<section class="abs" style="left:0;top:1724px;width:1200px;height:520px">
  <div class="abs" role="img" aria-label="Background of colourful woven Ethiopian baskets in red and orange tones" style="left:0;top:0;width:1200px;height:520px;background:linear-gradient(120deg,#e8452e,#d92f36 50%,#e5573a)"></div>
  <p class="abs center" style="left:150px;top:115px;width:432px;font-size:11.5px;font-weight:600;color:#fff;line-height:1.4">Lomi means health in Amharic, and also signifies a jewel basket: an expensive and unique gift to preserve.</p>
  <div class="abs center" style="left:100px;top:157px;width:532px;font-size:29px;font-weight:700;color:var(--yellow)">Seret means health in Hebrew.</div>
  <div class="abs center" style="left:166px;top:194px;width:400px;font-size:34px;font-weight:700;color:#fff;line-height:1.2">Health is a gift to be preserved</div>
  <div class="abs" role="img" aria-label="Traditional woven Ethiopian basket with a pointed lid" style="left:242px;top:310px;width:249px;height:234px;border-radius:50% 50% 45% 45%;background:radial-gradient(circle at 50% 55%,#e6b82a,#1f8a48 60%,#c92a2e);z-index:2"></div>
  <div class="abs frame" style="left:650px;top:106px;width:394px;height:306px">
    <div class="photo" role="img" aria-label="Photo of community members dancing together outdoors" style="left:22px;top:21px;width:350px;height:264px;background:linear-gradient(135deg,#8ea86e,#d7d3c9 50%,#6e6760)"></div>
  </div>
</section>

<!-- programs -->
<section class="abs" style="left:0;top:2244px;width:1200px;height:665px;background:linear-gradient(var(--cream) 0 345px,#fff 345px)">
  <div class="abs eyebrow center" style="top:78px">Lomi Seret</div>
  <h2 class="abs sec-title center" style="top:96px">Programs</h2>
</section>
<div class="abs card" style="left:150px">
  <div class="photo" role="img" aria-label="Health education presentation in a community hall" style="background:linear-gradient(135deg,#c8cdd4,#6d7884)"></div>
  <h4>Health &amp; Education<br>Presentations</h4>
  <p>To spread awareness of a health promoting lifestyle and an understanding of diabetes.</p>
  <span class="more">Read more »</span>
</div>
<div class="abs card" style="left:380px">
  <div class="photo" role="img" aria-label="Regional health fair with members at a registration table" style="background:linear-gradient(135deg,#d9c3c8,#8e5a66)"></div>
  <h4>Regional<br>Health Fairs</h4>
  <p>Every year, Lomi Seret holds approximately 5 regional health fairs where members...</p>
  <span class="more">Read more »</span>
</div>
<div class="abs card" style="left:610px">
  <div class="photo" role="img" aria-label="Radio studio during an Amharic radio broadcast" style="background:linear-gradient(135deg,#c7c2bd,#5d5753)"></div>
  <h4>Amharic<br>Radio Program</h4>
  <p>To reach the widest possible audience Lomi Seret produces a fortnightly radio program...</p>
  <span class="more">Read more »</span>
</div>
<div class="abs card" style="left:841px">
  <div class="photo" role="img" aria-label="Therapeutic support group exercising with red balls" style="background:linear-gradient(135deg,#b9c7d6,#d5d0c8 50%,#8c6f5d)"></div>
  <h4>Therapeutic<br>Support Groups</h4>
  <p>In partnership with Dr. Daniel Harlow, Bridges of Care, and Shalva Health...</p>
  <span class="more">Read more »</span>
</div>
<span class="abs btn btn-green" style="left:550px;top:2808px;width:100px;height:34px;font-size:9px">View more</span>

<!-- contact -->
<section class="abs" style="left:0;top:2909px;width:1200px;height:458px;background:var(--yellow)">
  <div class="abs center" style="left:0;top:66px;width:1200px;font-size:12px;color:#fff">Get Connected</div>
  <h2 class="abs center" style="left:0;top:84px;width:1200px;font-size:55px;font-weight:700;color:#fff">Contact Us</h2>
  <div class="abs field" style="left:225px;top:162px;width:244px;height:29px">Name:</div>
  <div class="abs field" style="left:478px;top:162px;width:244px;height:29px">Phone:</div>
  <div class="abs field" style="left:731px;top:162px;width:244px;height:29px">Email:</div>
  <div class="abs field" style="left:225px;top:202px;width:750px;height:121px;padding-top:14px">Describe your request:</div>
  <span class="abs btn btn-red" style="left:550px;top:345px;width:100px;height:33px;font-size:9px">Submit</span>
</section>

<!-- partners -->
<section class="abs sec-cream" style="left:0;top:3367px;width:1200px;height:145px">
  <div class="abs" style="left:246px;top:50px;width:56px;height:52px;border-radius:6px;background:#d9d2c8"></div>
  <div class="abs" style="left:352px;top:62px;width:88px;height:28px;border-radius:6px;background:#d9d2c8"></div>
  <div class="abs" style="left:500px;top:50px;width:66px;height:50px;border-radius:6px;background:#d9d2c8"></div>
  <div class="abs" style="left:634px;top:52px;width:72px;height:50px;border-radius:6px;background:#d9d2c8"></div>
  <div class="abs" style="left:762px;top:44px;width:44px;height:66px;border-radius:6px;background:#d9d2c8"></div>
  <div class="abs" style="left:864px;top:60px;width:96px;height:32px;border-radius:6px;background:#d9d2c8"></div>
</section>

<!-- footer contact -->
<section class="abs" style="left:0;top:3512px;width:1200px;height:463px;background:#fff">
  <div class="abs" style="left:490px;top:60px;width:220px;height:220px;border-radius:50%;border:3px solid var(--red);display:flex;align-items:center;justify-content:center;font-size:30px;font-weight:700;color:var(--red)">Lomi Seret</div>
  <div class="abs center" style="left:235px;top:318px;width:300px">
    <span class="ico" style="margin:0 auto"><svg width="11" height="11" viewBox="0 0 24 24"><path fill="#fff" d="M12 2a7 7 0 00-7 7c0 5 7 13 7 13s7-8 7-13a7 7 0 00-7-7zm0 9.5A2.5 2.5 0 1112 6a2.5 2.5 0 010 5.5z"/></svg></span>
    <div style="font-size:9px;margin-top:6px">office</div>
    <div style="font-size:10.5px;font-weight:600;color:var(--ink);margin-top:8px">Shaked 12/4 POB 4410 Hadera, 38200</div>
  </div>
  <div class="abs center" style="left:450px;top:318px;width:300px">
    <span class="ico" style="margin:0 auto"><svg width="11" height="11" viewBox="0 0 24 24"><path fill="#fff" d="M6.6 10.8a15 15 0 006.6 6.6l2.2-2.2c.3-.3.7-.4 1-.2 1.1.4 2.3.6 3.6.6.6 0 1 .4 1 1V20c0 .6-.4 1-1 1A17 17 0 013 4c0-.6.4-1 1-1h3.5c.6 0 1 .4 1 1 0 1.3.2 2.5.6 3.6.1.3 0 .7-.2 1z"/></svg></span>
    <div style="font-size:9px;margin-top:6px">phone</div>
    <div style="font-size:18px;font-weight:600;color:var(--ink);margin-top:2px">04-5550182</div>
  </div>
  <div class="abs center" style="left:665px;top:318px;width:300px">
    <span class="ico" style="margin:0 auto"><svg width="11" height="11" viewBox="0 0 24 24"><path fill="#fff" d="M2 5h20v14H2zm2 2v.5l8 5 8-5V7z"/></svg></span>
    <div style="font-size:9px;margin-top:6px">email</div>
    <div style="font-size:10.5px;font-weight:600;color:var(--ink);margin-top:8px">lomiseret@example.org</div>
  </div>
</section>

<!-- call to action -->
<div class="abs stripe" style="top:3975px"><i style="background:var(--green)"></i><i></i><i></i></div>
<section class="abs" style="left:0;top:3982px;width:1200px;height:217px;background:linear-gradient(90deg,var(--green-dark),var(--green))">
  <h2 class="abs center" style="left:0;top:40px;width:1200px;font-size:55px;font-weight:700;color:#fff">What You Can Do</h2>
  <span class="abs btn btn-red" style="left:541px;top:126px;width:118px;height:34px;font-size:10px">Support Us</span>
</section>

<!-- footer -->
<footer class="abs footer">
  <div class="fcol" style="left:167px">Home<br>The Community<br>Advocacy<br>Partners<br>Support Us<br>News</div>
  <div class="fcol" style="left:343px"><h5>About</h5>Board<br>Team<br>Missions and Goals</div>
  <div class="fcol" style="left:533px"><h5>Programs</h5>Health Education Presentations<br>Regional Health Fairs<br>Amharic Radio Program<br>Health Leadership Development<br>Nutrition &amp; Cookery Courses<br>Healthcare Personnel Training<br>Research &amp; Data Collection<br>Health Resources<br>Phone Survey</div>
  <div class="fcol" style="left:823px"><h5>Subscribe to our newsletter</h5></div>
  <div class="abs" style="left:823px;top:112px;width:225px;height:34px;background:#3a3a3a;display:flex;align-items:center">
    <span style="flex:1;padding-left:16px;font-size:9px;color:#ccc">your email address</span>
    <span style="width:46px;height:34px;background:var(--red);display:flex;align-items:center;justify-content:center;font-size:12px;font-weight:700">SEND</span>
  </div>
  <div class="abs" style="left:167px;top:476px;font-size:10px;color:#ddd">Copyright © 2022 Lomi Seret. All Rights Reserved</div>
  <div class="abs" style="left:990px;top:462px;display:flex;align-items:center;gap:6px;font-size:11px;font-weight:700;color:#fff"><span style="width:14px;height:14px;border-radius:50%;background:var(--red)"></span>Lomi Seret</div>
</footer>

</body>
</html>
```